Product Designer Business Card

Small product design, engineering and prototyping firm in need of a clean, professional business card design. To support our 3D design and drawing services, we offer 3D printing, molding, and casting of plastics, silicones, resins, etc. Our logo can still be modified/changed if necessary. The red/orange color is preferred, but may be substituted with blue or green, potentially. Either way, the colour of the logo should be match/compliment colors used throughout the design. One thought is to have the logo/contact info on one side, with the other side describing services offered, like with a small icon of 3D printer, molding, casting, and computer with a 3D model on-screen.
Industry/Entity Type
Mechanical Engineering
Contact Information for Business Card
Company: Halvick Design
Phone: 613-582-4179
Email: myles@halvickdesign.ca

```html
<!DOCTYPE html>
<html lang="en">
<head>
<meta charset="utf-8">
<title>Halvick Design – Business Card</title>
<link rel="stylesheet" href="https://fonts.googleapis.com/css2?family=Open+Sans:wght@400;600&display=swap">
<style>
  :root {
    --page: #8a8a8a;
    --card: #1c1c1c;
    --card-back: #1f1f1f;
    --icon-light: #3a3a3a;
    --icon-dark: #262626;
    --red: #e0262b;
    --white: #f2f2f2;
    --grey: #cfcfcf;
  }
  * { box-sizing: border-box; margin: 0; padding: 0; }
  html, body { width: 1200px; height: 1021px; overflow: hidden; }
  body {
    background: var(--page);
    font-family: "Open Sans", sans-serif;
    position: relative;
  }
  .card {
    position: absolute;
    left: 220px;
    width: 760px;
    height: 434px;
    box-shadow: 0 10px 30px rgba(0,0,0,0.35);
  }
  .card--services { top: 56px; background: var(--card-back); }
  .card--contact { top: 531px; background: var(--card); }

  .services {
    position: absolute;
    left: 50px; right: 50px; top: 0; bottom: 0;
    display: flex;
    align-items: center;
    justify-content: space-between;
  }
  .service { width: 150px; text-align: center; }
  .service__icon {
    width: 132px; height: 132px;
    margin: 0 auto 12px;
    background: radial-gradient(circle at 50% 45%, var(--icon-light), var(--icon-dark) 75%);
    border-radius: 8px;
  }
  .service__label { color: var(--red); font-size: 20px; line-height: 26px; }

  .brand {
    position: absolute;
    top: 90px; left: 0; right: 0;
    display: flex; align-items: center; justify-content: center; gap: 18px;
  }
  .brand__dot { width: 58px; height: 58px; border-radius: 50%; background: var(--red); }
  .brand__name {
    color: var(--white);
    font-size: 44px; font-weight: 600;
    letter-spacing: 6px;
  }

  .person {
    position: absolute;
    right: 420px; top: 270px;
    text-align: right;
  }
  .person__name { color: var(--red); font-size: 28px; font-weight: 600; }
  .person__role { color: var(--white); font-size: 21px; margin-top: 2px; }

  .divider {
    position: absolute;
    left: 366px; top: 268px;
    width: 1.5px; height: 80px;
    background: var(--grey);
  }
  .contact {
    position: absolute;
    left: 388px; top: 266px;
    list-style: none;
  }
  .contact li {
    display: flex; align-items: center; gap: 10px;
    color: var(--white); font-size: 21px; line-height: 29px;
  }
  .contact svg { width: 18px; height: 18px; flex: none; }
</style>
</head>
<body>
  <section class="card card--services" aria-label="Services side">
    <div class="services">
      <div class="service">
        <div class="service__icon" role="img" aria-label="White line icon of a 3D printer"></div>
        <p class="service__label">3D Printing</p>
      </div>
      <div class="service">
        <div class="service__icon" role="img" aria-label="White line icon of a molding machine"></div>
        <p class="service__label">Molding</p>
      </div>
      <div class="service">
        <div class="service__icon" role="img" aria-label="White line icon of material being poured into a casting mold"></div>
        <p class="service__label">Casting</p>
      </div>
      <div class="service">
        <div class="service__icon" role="img" aria-label="White line icon of a computer showing a 3D model"></div>
        <p class="service__label">3d Model</p>
      </div>
    </div>
  </section>

  <section class="card card--contact" aria-label="Contact side">
    <div class="brand">
      <span class="brand__dot"></span>
      <span class="brand__name">Halvick Design</span>
    </div>

    <div class="person">
      <p class="person__name">Myles Brennan</p>
      <p class="person__role">Owner</p>
    </div>

    <div class="divider"></div>

    <ul class="contact">
      <li>
        <svg viewBox="0 0 24 24" aria-hidden="true"><path fill="#e0262b" d="M6.6 10.8a15 15 0 0 0 6.6 6.6l2.2-2.2a1 1 0 0 1 1-.25 11.4 11.4 0 0 0 3.6.57 1 1 0 0 1 1 1V20a1 1 0 0 1-1 1A17 17 0 0 1 3 4a1 1 0 0 1 1-1h3.5a1 1 0 0 1 1 1c0 1.25.2 2.45.57 3.57a1 1 0 0 1-.25 1z"/></svg>
        613-582-4179
      </li>
      <li>
        <svg viewBox="0 0 24 24" aria-hidden="true"><rect x="2.5" y="5" width="19" height="14" fill="none" stroke="#e0262b" stroke-width="2"/><path d="M2.5 5l9.5 8 9.5-8" fill="none" stroke="#e0262b" stroke-width="2"/></svg>
        myles@halvickdesign.ca
      </li>
      <li>
        <svg viewBox="0 0 24 24" aria-hidden="true"><g fill="none" stroke="#e0262b" stroke-width="1.8"><circle cx="12" cy="12" r="9.5"/><ellipse cx="12" cy="12" rx="4.5" ry="9.5"/><path d="M2.5 12h19M4 7h16M4 17h16"/></g></svg>
        www.halvickdesign.ca
      </li>
    </ul>
  </section>
</body>
</html>
```